Zirkus Design (Hintergrund)
Zielgruppe
Familien, Eltern, Kinder (Jugendliche), LehrerInnen / Pädagogen, päd. Einrichtungen, Firmen
kreativ, künstlerisch, welt offen, international, sozial, engagiert, sportlich
Aufgabenstellung
Das Layout soll multifunktional sein, das heist in seinen Grundzügen oder leicht abgewandelt soll es für Postkarten, Flyer (DIN A 4 3 fach geknickt) und evtl. Plakate (als Hintergrund) Verwendung finden.
Und es soll für verschiedene Projekte / Veranstaltungen wiederverwendet werden, da ich nicht das Budget habe jedesmal ein neues Layout machen zu lassen.

```html
<!DOCTYPE html>
<html lang="de">
<head>
<meta charset="utf-8">
<title>Zirkus – Programm 15. bis 27. Dezember</title>
<link rel="stylesheet" href="https://fonts.googleapis.com/css2?family=Short+Stack&display=swap">
<style>
  :root {
    --cream: #fdf9e3;
    --green-dark: #0f6b2e;
    --green: #1c8a3c;
    --green-light: #4fae3f;
    --yellow: #f6d21a;
    --orange: #f7a41c;
    --pink: #e4407c;
    --ink: #1d1d1b;
    --fold: #d9d4bd;
    --juggler: #f5c12c;
  }
  * { margin: 0; padding: 0; box-sizing: border-box; }
  html, body { width: 1200px; height: 848px; overflow: hidden; background: #ffffff; }
  .flyer {
    position: relative;
    width: 1200px; height: 848px;
    overflow: hidden;
    background: var(--cream);
    font-family: "Short Stack", cursive;
    color: var(--ink);
  }
  .backdrop { position: absolute; inset: 0; }
  .fold { position: absolute; top: 0; bottom: 0; width: 1px; background: var(--fold); }
  .fold--one { left: 400px; }
  .fold--two { left: 800px; }

  .brand {
    position: absolute; left: 30px; top: 48px;
    display: flex; align-items: center; gap: 10px;
    color: var(--green-light);
    font-size: 26px; line-height: 1;
  }
  .brand__dot { width: 16px; height: 16px; border-radius: 50%; background: var(--pink); }

  .headline {
    position: absolute; left: 462px; top: 44px;
    font-family: "Short Stack", cursive;
    font-weight: 400;
    font-size: 40px; line-height: 1;
    color: var(--green);
  }

  .photo { position: absolute; }
  .photo--aerial { left: 88px; top: 284px; width: 285px; height: 200px;
    background: radial-gradient(circle at 60% 40%, #f7b430 0%, #c45a13 45%, #2a1408 100%); }
  .photo--dancers { left: 447px; top: 175px; width: 293px; height: 191px;
    background: linear-gradient(180deg, #3b2b4a 0%, #c84f7a 50%, #e9d5e0 100%); }
  .photo--lion { left: 824px; top: 264px; width: 297px; height: 228px;
    background: radial-gradient(circle at 50% 55%, #c08a4a 0%, #4a2a16 55%, #120c08 100%); }

  .juggler {
    position: absolute; left: 530px; top: 370px; width: 170px; height: 380px;
    border-radius: 85px 85px 20px 20px;
    background: var(--juggler); opacity: 0.4;
  }
  .kids { position: absolute; background: var(--green-dark); border-radius: 34px 34px 0 0; }
  .kids--left { left: 4px; top: 652px; width: 78px; height: 88px; }
  .kids--right { left: 1050px; top: 662px; width: 132px; height: 76px; }

  .column { position: absolute; top: 0; font-size: 14px; line-height: 21px; hyphens: manual; }
  .column p { position: absolute; left: 0; width: 100%; }
  .column--left { left: 88px; width: 300px; }
  .column--middle { left: 439px; width: 315px; }
  .column--right { left: 824px; width: 300px; }

  .footer-note {
    position: absolute; left: 215px; top: 784px; width: 770px;
    text-align: center;
    color: var(--pink);
    font-size: 12.5px; line-height: 27px;
  }
</style>
</head>
<body>
<div class="flyer">

  <svg class="backdrop" width="1200" height="848" viewBox="0 0 1200 848" aria-hidden="true">
    <defs>
      <linearGradient id="bandGreen" x1="0" y1="0" x2="0" y2="1">
        <stop offset="0" stop-color="#1d8b3a"/>
        <stop offset="1" stop-color="#0f6b2e"/>
      </linearGradient>
      <radialGradient id="panelGlow" cx="0.5" cy="0.55" r="0.6">
        <stop offset="0" stop-color="#fbf0b0"/>
        <stop offset="1" stop-color="#fffbe8"/>
      </radialGradient>
    </defs>
    <rect x="0" y="132" width="1200" height="10" fill="var(--yellow)"/>
    <rect x="0" y="142" width="1200" height="620" fill="url(#bandGreen)"/>
    <path d="M40 230 Q40 165 120 162 Q600 150 1080 162 Q1160 165 1160 230 L1160 738 Q600 770 40 738 Z"
          fill="url(#panelGlow)" stroke="var(--green-light)" stroke-width="3"/>
    <path d="M0 728 Q600 790 1200 728 L1200 848 L0 848 Z" fill="var(--green-dark)"/>
    <path d="M0 742 Q600 800 1200 742 L1200 848 L0 848 Z" fill="var(--yellow)"/>
    <path d="M0 752 Q600 808 1200 752 L1200 848 L0 848 Z" fill="var(--orange)"/>
  </svg>

  <div class="fold fold--one"></div>
  <div class="fold fold--two"></div>

  <div class="brand">
    <span class="brand__dot"></span>
    <span class="brand__name">Zirkus Jonas Wendt</span>
  </div>

  <h1 class="headline">Programm 15. bis 27. Dezember</h1>

  <div class="juggler" role="img" aria-label="Silhouette eines Jongleurs mit Ringen"></div>
  <div class="kids kids--left" role="img" aria-label="Silhouette staunender Kinder"></div>
  <div class="kids kids--right" role="img" aria-label="Silhouette einer Familie"></div>

  <div class="photo photo--aerial" role="img" aria-label="Foto: Luftakrobatik im Rhönrad unter bunten Scheinwerfern"></div>
  <div class="photo photo--dancers" role="img" aria-label="Foto: Clown mit Tänzerinnen in Kostümen in der Manege"></div>
  <div class="photo photo--lion" role="img" aria-label="Foto: Dressurnummer in der Manege"></div>

  <div class="column column--left">
    <p style="top:222px">Pellentesque eu mauris vitae libero pellen&shy;tesque aliquam.</p>
    <p style="top:505px">Suspendisse sollicitudin blandit convallis. Suspendisse elementum condi&shy;mentum ullamcorper.</p>
    <p style="top:608px">Aliquam erat volutpat. In tempor varius scelerisque.</p>
  </div>

  <div class="column column--middle">
    <p style="top:398px">Pellentesque eu mauris vitae libero pellen&shy;tesque aliquam.</p>
    <p style="top:475px">Suspendisse sollicitudin blandit convallis. Suspendisse elementum condi&shy;mentum ullamcorper.</p>
    <p style="top:578px">Aliquam erat volutpat. In tempor varius scelerisque.</p>
    <p style="top:655px">Donec egestas, sem eu gravida sceleris&shy;que, risus nisi convallis nisl, eget pellen&shy;tesque nisi nisl quis lacus.</p>
  </div>

  <div class="column column--right">
    <p style="top:202px">Pellentesque eu mauris vitae libero pellentesque aliquam.</p>
    <p style="top:508px">Suspendisse sollicitudin blandit convallis. Suspendisse elementum condi&shy;mentum ullamcorper.</p>
    <p style="top:605px">Aliquam erat volutpat. In tempor varius scelerisque.</p>
    <p style="top:687px">Donec egestas, sem eu</p>
  </div>

  <p class="footer-note">Morbi ut metus nibh, non tristique enim. Proin pretium auctor purus. Nulla facilisi. Donec feugiat mattis eleifend. In faucibus nulla non mauris egestas dignissim. Suspendisse eros</p>

</div>
</body>
</html>
```